Business Card Design, including supply of raw art files plus a vector diagram of the zelvon logo and

We need the business card design for a company that is launching a new exciting product. The brief requires the submission of the following once the final design is chosen:

- business card layout including raw files
- a composite vector image file of the zelvon logo and tag line
- a standalone vector image file of the zelvon logo

The product will be launched as a customer engagement app.

It has 4 core modules which enables a person to do multiple things - book tours and activities, order takeaways, search for local deals and offers. A universal currency is at the heart of this product. When you use the app, you earn cashback rewards when shopping or buying at any of the merchant partners across the modules as . These rewards can then be used as full or part payment when buying goods or services at these merchant partners.

The business card must help us build the brand, communicate the benefit of the brand's key focus - the ability to earn and burn this universal cashback ccurrency - across the 4 modules - booking of tours and activities, ordering, searching for local deals and payment.

We would like the design to use the brand's blue colour the hex colour is: 00
Dark grey : 646464
Darker blue shadow: 058bdd
Main Blue: 0084ff

We need to translate this into a CMYK print or spot colour print.

Both print options to be supplied as separate files.

An example of the base concept we have in mind is attached for your reference.

The font used by the brand is Proxima Nova.

Note: the duration has been set as 2 days.

Industry/Entity Type

Business

Contact Information for Business Card

Carla Mendoza
Marketing
W: www.zelvon.example
M: + 61 400555123
T: +61 2 5550 1473
A: Suite 7, Level 2, 14-18 Harwick Street, Sydney, NSW, 2000, Australia

Font styles to use
Sans Serif

Requirements
Must have
• zelvon logo and tagline
• address details
• zelvon icons as supplied
Nice to have
• would like to have the option of a spot varnish layer over the logo and icons at the back of the card

```html
<!DOCTYPE html>
<html lang="en">
<head>
<meta charset="utf-8">
<title>zelvon business card</title>
<link href="https://fonts.googleapis.com/css2?family=Open+Sans:wght@400;600;700&display=swap" rel="stylesheet">
<style>
  :root {
    --brand-blue: #2b8ed8;
    --icon-blue: #1566b4;
    --accent-blue: #1e8ad6;
    --dark-grey: #646464;
    --ink: #333333;
    --paper: #ffffff;
    --backdrop: #e9eaec;
    --rule: #555555;
  }
  * { margin: 0; padding: 0; box-sizing: border-box; }
  html, body { width: 1200px; height: 900px; overflow: hidden; }
  body {
    background: var(--backdrop);
    font-family: "Open Sans", Arial, sans-serif;
    position: relative;
  }
  .card {
    position: absolute;
    width: 620px;
    height: 380px;
    box-shadow: 0 6px 18px rgba(0,0,0,0.18);
    overflow: hidden;
  }
  /* Back of card */
  .card-back { left: 90px; top: 50px; background: var(--brand-blue); color: var(--paper); }
  .brand-lockup { position: absolute; display: flex; align-items: center; gap: 16px; }
  .card-back .brand-lockup { left: 190px; top: 135px; }
  .brand-mark { width: 70px; height: 70px; border-radius: 50%; flex: none; }
  .card-back .brand-mark { background: var(--paper); }
  .brand-name { font-weight: 600; font-size: 44px; line-height: 1; }
  .brand-tagline { font-weight: 400; font-size: 13px; letter-spacing: 0.3px; margin-top: 6px; }
  .feature { position: absolute; display: flex; flex-direction: column; align-items: center; width: 130px; }
  .feature-icon {
    width: 52px; height: 52px; border-radius: 50%; background: var(--icon-blue);
    display: flex; align-items: center; justify-content: center;
  }
  .feature-label { font-size: 11px; margin-top: 6px; white-space: nowrap; }
  .feature-ordering { left: 20px; top: 150px; }
  .feature-cashback { left: 60px; top: 235px; }
  .feature-tours { left: 470px; top: 30px; }
  .feature-offers { left: 505px; top: 105px; }
  .back-url {
    position: absolute; left: 0; right: 0; bottom: 38px; text-align: center;
    font-size: 17px; letter-spacing: 3px;
  }
  /* Front of card */
  .card-front { left: 490px; top: 470px; background: var(--paper); color: var(--ink); }
  .card-front .brand-lockup { left: 40px; top: 60px; }
  .card-front .brand-mark { background: var(--accent-blue); }
  .card-front .brand-name { color: var(--dark-grey); }
  .card-front .brand-tagline { color: var(--dark-grey); }
  .address {
    position: absolute; right: 36px; top: 70px; text-align: right;
    font-size: 15px; line-height: 1.35; color: var(--ink); font-style: normal;
  }
  .divider { position: absolute; left: 40px; right: 36px; top: 160px; height: 1.5px; background: var(--rule); }
  .person { position: absolute; left: 40px; top: 182px; }
  .person-name { color: var(--accent-blue); font-weight: 700; font-size: 21px; letter-spacing: 0.3px; }
  .person-role { font-size: 18px; margin-top: 2px; }
  .person-rule { width: 190px; height: 1.5px; background: var(--rule); margin-top: 14px; }
  .contacts { list-style: none; margin-top: 12px; }
  .contacts li { display: flex; align-items: center; gap: 8px; font-size: 16px; line-height: 1.45; }
  .contact-icon {
    width: 16px; height: 16px; border-radius: 50%; background: var(--accent-blue);
    display: inline-flex; align-items: center; justify-content: center; flex: none;
  }
</style>
</head>
<body>

<section class="card card-back" aria-label="Card back">
  <div class="brand-lockup">
    <span class="brand-mark"></span>
    <div>
      <div class="brand-name">zelvon</div>
      <div class="brand-tagline">rewards you can spend</div>
    </div>
  </div>

  <div class="feature feature-ordering">
    <span class="feature-icon">
      <svg width="26" height="26" viewBox="0 0 26 26" fill="none" stroke="#fff" stroke-width="2" stroke-linecap="round">
        <line x1="6" y1="5" x2="20" y2="22"/><line x1="20" y1="5" x2="6" y2="22"/>
        <ellipse cx="19" cy="7" rx="2.5" ry="3.5" fill="#fff"/>
      </svg>
    </span>
    <span class="feature-label">Mobile Ordering</span>
  </div>

  <div class="feature feature-cashback">
    <span class="feature-icon">
      <svg width="26" height="26" viewBox="0 0 26 26" fill="none" stroke="#fff" stroke-width="2" stroke-linecap="round">
        <path d="M5 11a8 8 0 0 1 14-4"/><polyline points="19,3 19,7 15,7"/>
        <path d="M21 15a8 8 0 0 1-14 4"/><polyline points="7,23 7,19 11,19"/>
        <text x="13" y="17" font-size="9" fill="#fff" stroke="none" text-anchor="middle" font-family="Arial, sans-serif">$</text>
      </svg>
    </span>
    <span class="feature-label">CashBack Rewards</span>
  </div>

  <div class="feature feature-tours">
    <span class="feature-icon">
      <svg width="26" height="26" viewBox="0 0 26 26" fill="none" stroke="#fff" stroke-width="2">
        <rect x="3" y="8" width="20" height="13" rx="2"/><path d="M9 8l2-3h4l2 3"/><circle cx="13" cy="14.5" r="3.5"/>
      </svg>
    </span>
    <span class="feature-label">Tours &amp; Activities</span>
  </div>

  <div class="feature feature-offers">
    <span class="feature-icon">
      <svg width="26" height="26" viewBox="0 0 26 26">
        <path d="M9 4h8l3 5v12H6V9z" fill="#fff"/><circle cx="13" cy="9" r="1.6" fill="#1566b4"/>
      </svg>
    </span>
    <span class="feature-label">Local Offers</span>
  </div>

  <div class="back-url">www.zelvon.example</div>
</section>

<section class="card card-front" aria-label="Card front">
  <div class="brand-lockup">
    <span class="brand-mark"></span>
    <div>
      <div class="brand-name">zelvon</div>
      <div class="brand-tagline">rewards you can spend</div>
    </div>
  </div>

  <address class="address">
    Suite 7, Level 2,<br>
    14-18 Harwick Street, Sydney,<br>
    NSW, 2000, Australia
  </address>

  <div class="divider"></div>

  <div class="person">
    <div class="person-name">CARLA MENDOZA</div>
    <div class="person-role">Marketing</div>
    <div class="person-rule"></div>
    <ul class="contacts">
      <li>
        <span class="contact-icon"><svg width="8" height="10" viewBox="0 0 8 10"><rect x="1" y="0.5" width="6" height="9" rx="1" fill="none" stroke="#fff"/></svg></span>
        + 61 400555123
      </li>
      <li>
        <span class="contact-icon"><svg width="10" height="8" viewBox="0 0 10 8"><rect x="0.5" y="2" width="9" height="5.5" rx="1" fill="#fff"/><rect x="2" y="0.5" width="6" height="2" fill="none" stroke="#fff"/></svg></span>
        +61 2 5550 1473
      </li>
      <li>
        <span class="contact-icon"><svg width="10" height="10" viewBox="0 0 10 10" fill="none" stroke="#fff" stroke-width="0.9"><circle cx="5" cy="5" r="4"/><ellipse cx="5" cy="5" rx="1.8" ry="4"/><line x1="1" y1="5" x2="9" y2="5"/></svg></span>
        www.zelvon.example
      </li>
    </ul>
  </div>
</section>

</body>
</html>
```